LITTLE DESIGN WORK REQUIRED!

UPDATE: WE WEREN'T OVERLY ECSTATIC WITH THE DESIGNS WE WERE RECEIVING SO WE DID MOST OF THE DESIGN WORK OURSELVES...

PLEASE SEE THE NEWLY ATTACHED PPT DOC TO VIEW NEARLY EXACT REPLICAS OF WHAT WE WANT THE SITE TO LOOK LIKE. WE NOW NEED YOUR HELP TO MAKE IT LOOK LIKE SOMETHING WORTHY OF THE WEB.

NO CODING REQUIRED - EXPECTED OUTPUT PSD FILES

Hi everyone!

We're looking for a designer to work their magic for our site! We're a not-for-profit program aimed at helping young people realise their potential!

In the attached PPT file, you'll notice we've already DESIGNED THE ENTIRE SITE IN POWERPOINT. Now, we need YOU to make the small changes we requested in the document as well as design the whole thing in psd.

Any questions, don't hesitate to ask.

Brook-Rise
Updates

We've done about 95% of the design for you. Please fine-tune it. See the newly attached PPT doc for details. 

The best two designs will win. This project closes on Friday - please message us if you are absolutely sure you cannot make the deadline.

Thanks,
Brook-Rise

```html
<!DOCTYPE html>
<html lang="en">
<head>
<meta charset="utf-8">
<title>Brook-Rise</title>
<link href="https://fonts.googleapis.com/css2?family=Ubuntu:wght@400;500;700&family=Oswald:wght@500&family=Arimo:wght@400;700&display=swap" rel="stylesheet">
<style>
:root{
  --green:#7fbb14;
  --green-light:#9ad12a;
  --green-dark:#62980a;
  --ink:#222;
  --text:#444;
  --muted:#888;
  --page:#ececec;
  --panel:#f7f7f7;
  --dark:#1d1d1d;
  --dark-2:#2a2a2a;
  --fb-blue:#3b5998;
  --link-blue:#3b5998;
}
*{box-sizing:border-box;margin:0;padding:0}
html,body{width:960px;height:1200px;overflow:hidden}
body{background:var(--page);font-family:"Arimo",Arial,sans-serif;color:var(--text);position:relative}
.abs{position:absolute}
.topbar{left:0;top:0;width:960px;height:18px;background:var(--dark)}
.social{left:718px;top:0;width:161px;height:38px;background:var(--dark);display:flex;gap:4px;padding:4px 7px}
.social span{width:34px;height:28px;background:var(--green);display:block}
.brand{left:86px;top:58px;font-family:"Ubuntu",sans-serif;font-weight:700;font-size:38px;color:var(--ink);letter-spacing:1px;display:flex;align-items:center;gap:10px}
.brand i{width:18px;height:18px;border-radius:50%;background:var(--green);display:block}
.enquiries{right:85px;top:108px;font-family:"Oswald",sans-serif;font-size:20px;color:#555;display:flex;align-items:center;gap:6px}
.enquiries b{color:var(--green);font-weight:500}
.enquiries i{width:14px;height:14px;background:var(--green);display:block;border-radius:50%}
.main{left:80px;top:150px;width:800px;height:932px;background:var(--panel);box-shadow:0 0 3px rgba(0,0,0,.12)}
.nav{left:80px;top:150px;width:800px;height:40px;font-family:"Ubuntu",sans-serif;font-weight:500;font-size:12.5px;color:#555;letter-spacing:.5px}
.nav a{position:absolute;top:8px;color:#555;text-decoration:none}
.nav .home{left:27px;top:-10px;width:82px;height:46px;background:linear-gradient(var(--green-light),var(--green));color:#fff;text-align:center;padding-top:18px}
.hero{left:82px;top:233px;width:796px;height:313px;border:4px solid var(--green);background:#fff}
.hero-photo{left:4px;top:4px;width:530px;height:297px;background:linear-gradient(90deg,#e9e6e3,#f4f4f4 60%,#fafafa)}
.register{left:620px;top:198px;width:240px}
.register svg{position:absolute;left:0;top:0}
.search{left:638px;top:207px;width:196px;height:25px;background:#fff;border-radius:4px;font-size:9.5px;color:#888;padding:7px 14px}
.search i{position:absolute;right:0;top:0;width:32px;height:25px;background:#e2e2e2;border-radius:0 4px 4px 0}
.register-title{left:639px;top:251px;font-family:"Ubuntu",sans-serif;font-weight:500;font-size:19px;color:#fff}
.register-title b,.hl{color:var(--green);font-weight:500}
.field{left:633px;width:211px;height:22px;background:#fff;border-radius:11px;font-family:"Ubuntu",sans-serif;font-size:10px;color:#777;padding:5px 16px}
.reg-btn{left:680px;top:459px;width:124px;height:28px}
.welcome{left:93px;top:569px;font-family:"Ubuntu",sans-serif;font-weight:500;font-size:20px;color:#555}
.intro{left:93px;width:543px;font-size:9.8px;line-height:16px;letter-spacing:.3px;color:#555}
.intro b{color:var(--ink);letter-spacing:0}
.steps{left:88px;top:726px;width:548px;height:95px;background:#fff;border:1px solid #ddd}
.steps svg{position:absolute;left:1px;top:1px}
.posts-icon{left:94px;top:837px;width:40px;height:40px;border-radius:6px;background:linear-gradient(#9ad12a,#6aa10b)}
.section-title{font-family:"Ubuntu",sans-serif;font-weight:500;font-size:18px;color:#555}
.sub{left:92px;top:890px;font-family:"Ubuntu",sans-serif;font-size:13px;color:#444}
.post-photo{left:90px;top:917px;width:156px;height:136px;border:3px solid #fff;box-shadow:0 0 2px rgba(0,0,0,.3);background:linear-gradient(135deg,#a9785a,#d8c7b3 50%,#8f6a4b)}
.post-title{left:260px;top:917px;font-family:"Ubuntu",sans-serif;font-weight:500;font-size:14.5px;color:var(--green)}
.post-text{left:260px;top:942px;width:375px;font-size:8.6px;line-height:16px;color:#333;text-align:justify}
.readmore{left:565px;top:1053px;font-family:"Ubuntu",sans-serif;font-weight:500;font-size:10px;color:var(--green-dark)}
.fb{left:663px;top:578px;width:211px;height:240px;background:#fff;border:1px solid #ccd}
.fb-head{height:27px;background:var(--fb-blue);color:#fff;display:flex;justify-content:space-between;align-items:center;padding:0 6px}
.fb-head b{font-family:"Arimo",sans-serif;font-size:15px}
.fb-head span{font-size:9px}
.fb-page{position:absolute;left:6px;top:36px;font-family:"Ubuntu",sans-serif;font-weight:700;font-size:11px;color:var(--ink)}
.fb-name{position:absolute;left:74px;top:39px;font-size:10px;color:var(--link-blue);letter-spacing:.6px}
.fb-like{position:absolute;left:72px;top:53px;font-size:8.5px;color:#333;display:flex;gap:5px;align-items:center}
.fb-like span{border:1px solid #bbb;background:#eef;color:var(--link-blue);padding:1px 4px;border-radius:2px}
.fb-list{position:absolute;left:4px;top:74px;width:200px;border-top:1px solid #e5e5e5}
.fb-item{height:33px;position:relative;margin-top:0}
.fb-item i{position:absolute;left:8px;top:5px;width:22px;height:22px;background:var(--fb-blue);border-radius:3px}
.fb-item b{position:absolute;left:38px;top:4px;font-size:8.6px;color:var(--link-blue);letter-spacing:.5px;font-weight:400}
.fb-item span{position:absolute;left:38px;top:17px;font-size:7.5px;color:#999}
.fb-foot{position:absolute;left:4px;top:220px;width:200px;border-top:1px solid #ddd;padding:5px 5px;font-size:7px;color:#555;display:flex;gap:4px;align-items:center}
.fb-foot i{width:9px;height:9px;background:var(--fb-blue);display:block}
.amb{left:672px;width:200px}
.amb .avatar{position:absolute;left:0;top:0;width:40px;height:40px;background:#fff;border:1px solid #ddd}
.amb .avatar span{position:absolute;left:6px;top:6px;width:26px;height:26px;border-radius:50%}
.amb h4{position:absolute;left:53px;top:-2px;font-family:"Ubuntu",sans-serif;font-weight:500;font-size:11px;color:var(--green-dark);letter-spacing:.5px}
.amb p{position:absolute;left:54px;top:11px;width:140px;font-family:"Ubuntu",sans-serif;font-size:8.8px;line-height:11px;color:#333;letter-spacing:.3px}
.amb a{position:absolute;left:134px;top:35px;font-family:"Ubuntu",sans-serif;font-style:italic;font-size:8.8px;color:var(--green);text-decoration:underline}
.footer{left:0;top:1102px;width:960px;height:98px;background:var(--dark-2)}
.foot-links{left:103px;top:1133px;font-family:"Ubuntu",sans-serif;font-size:10.5px;color:#ccc;letter-spacing:.4px;word-spacing:2px}
.foot-copy{left:103px;top:1153px;font-family:"Ubuntu",sans-serif;font-size:11px;color:#eee}
.contact-icon{left:642px;top:1099px;width:26px;height:26px;background:#c9a55a;border:2px solid #eee;border-radius:3px}
.contact-title{left:675px;top:1106px;font-family:"Ubuntu",sans-serif;font-weight:700;font-size:16px;color:#fff}
.contact-title b{color:var(--green)}
.contact-rule{left:640px;top:1135px;width:240px;border-top:1px dotted #555}
.address{left:665px;top:1151px;font-family:"Ubuntu",sans-serif;font-size:11px;line-height:19px;color:#eee;letter-spacing:.3px}
</style>
</head>
<body>
<div class="abs topbar"></div>
<div class="abs social" aria-label="Social links"><span></span><span></span><span></span><span></span></div>

<div class="abs brand"><i></i>BROOK RISE</div>
<div class="abs enquiries"><i></i><b>Enquiries:</b> +61 (3) 5550 1827</div>

<div class="abs main"></div>
<nav class="abs nav">
  <a class="home">Home</a>
  <a style="left:149px">About Us</a>
  <a style="left:255px">Resources</a>
  <a style="left:371px">Article</a>
  <a style="left:474px">Work-shops</a>
  <a style="left:601px">Ambassadors</a>
  <a style="left:757px">Feats</a>
</nav>

<section class="abs hero">
  <div class="abs hero-photo" role="img" aria-label="Photo of a smiling young woman holding a clipboard with three young students standing behind her"></div>
</section>

<div class="abs register">
  <svg width="240" height="322" viewBox="0 0 240 322">
    <path d="M8 0 H230 Q240 0 240 10 V300 L120 322 L0 300 V40 Q0 0 8 0Z" fill="#1d1d1d"/>
    <path d="M0 40 Q-20 30 -22 44 L0 44Z" fill="#bbb"/>
    <path d="M116 298 L124 298 L120 304Z" fill="#fff"/>
  </svg>
</div>
<div class="abs search">Enter Keyword<i></i></div>
<div class="abs register-title"><b>Register</b> Now</div>
<div class="abs field" style="top:287px">Usrename :</div>
<div class="abs field" style="top:319px">Password Re- Password :</div>
<div class="abs field" style="top:351px">Email Address :</div>
<div class="abs field" style="top:383px">Conferm Email Address :</div>
<div class="abs field" style="top:415px">Country Name :</div>
<svg class="abs reg-btn" viewBox="0 0 124 28">
  <defs><linearGradient id="btn" x1="0" y1="0" x2="0" y2="1"><stop offset="0" stop-color="#a5d93a"/><stop offset="1" stop-color="#5f960a"/></linearGradient></defs>
  <path d="M12 1 H112 L123 14 L112 27 H12 L1 14Z" fill="url(#btn)" stroke="#e8f5c8" stroke-width="1.5"/>
  <text x="62" y="18.5" text-anchor="middle" font-family="Ubuntu, sans-serif" font-weight="500" font-size="12.5" fill="#fff">Register <tspan fill="#e3f3b4">Now</tspan></text>
</svg>

<h1 class="abs welcome"><span class="hl">Welcome to</span> Brook-Rise</h1>
<p class="abs intro" style="top:600px"><b>Brook-rise is a not-for-profit program aimed at helping people</b> – especially young people – realise their potential and achieve success. Brook-rise is a not-for-profit program aimed at helping people – especially young people – realise their potential and achieve success.</p>
<p class="abs intro" style="top:664px"><b>Our resources are categorised into four groups: discovery,</b> design, build, and achieve – the four steps in our achievement framework. Our resources are categorised into four groups: discovery, design, build, and achieve – the four steps in our achievement framework.</p>

<div class="abs steps">
  <svg width="544" height="91" viewBox="0 0 544 91">
    <defs><linearGradient id="step" x1="0" y1="0" x2="0" y2="1"><stop offset="0" stop-color="#93cb1e"/><stop offset="1" stop-color="#629a09"/></linearGradient></defs>
    <path d="M3 3 H115 L133 45.5 L115 88 H3Z" fill="url(#step)"/>
    <path d="M142 3 H254 L272 45.5 L254 88 H142 L160 45.5Z" fill="url(#step)"/>
    <path d="M282 3 H394 L412 45.5 L394 88 H282 L300 45.5Z" fill="url(#step)"/>
    <path d="M422 3 H541 V88 H422 L440 45.5Z" fill="url(#step)"/>
    <g font-family="Ubuntu, sans-serif" font-weight="500" font-size="19" fill="#fff" text-anchor="middle">
      <text x="63" y="52">Discover</text>
      <text x="205" y="52">Design</text>
      <text x="345" y="52">Build</text>
      <text x="484" y="52">Achieve</text>
    </g>
  </svg>
</div>

<div class="abs posts-icon" role="img" aria-label="Feed icon with a reader"></div>
<h2 class="abs section-title" style="left:142px;top:846px"><span class="hl">Recent</span> Posts</h2>
<p class="abs sub">Our resources are categorised into four groups: discovery, design.</p>
<div class="abs post-photo" role="img" aria-label="Photo of students studying together at a table"></div>
<h3 class="abs post-title">Brook-rise is a not-for-profit program aimed</h3>
<p class="abs post-text"><b>Lorem Ipsum is simply dummy text of the printing and typesetting industry. Lorem Ipsum has been the industry's standard dummy</b> text ever since the 1500s, when an unknown printer took a galley of type and scrambled it to make a type specimen book. It has survived not only five centuries, but also the leap into electronic typesetting, remaining essentially unchanged. when an unknown printer took a galley of type and scrambled it to make a type specimen book. It has survived not only five centuries, but also the leap into electronic typesetting, remaining essentially unchanged.</p>
<div class="abs readmore">Readmore[+]</div>

<aside class="abs fb">
  <div class="fb-head"><b>friendline</b><span>Find us on Friendline</span></div>
  <div class="fb-page">BROOK RISE</div>
  <div class="fb-name">Brook Rise</div>
  <div class="fb-like"><span>Like</span>3,564 peaple like this.</div>
  <div class="fb-list">
    <div class="fb-item"><i></i><b>Eat plain popcorn when you are</b><span>3,564 peaple Shared this.</span></div>
    <div class="fb-item"><i></i><b>Eat plain popcorn when you are</b><span>3,564 peaple Shared this.</span></div>
    <div class="fb-item"><i></i><b>Eat plain popcorn when you are</b><span>3,564 peaple Shared this.</span></div>
    <div class="fb-item"><i></i><b>Eat plain popcorn when you are</b><span>3,564 peaple Shared this.</span></div>
  </div>
  <div class="fb-foot"><i></i>Friendline social plugin</div>
</aside>

<h2 class="abs section-title" style="left:674px;top:845px"><span class="hl">Amb</span>assadors</h2>
<div class="abs amb" style="top:880px;height:45px">
  <div class="avatar"><span style="background:#7fbb14" role="img" aria-label="Ambassador portrait"></span></div>
  <h4>John Doe</h4><p>Lorem ipsum dolor sit amet, consectetur</p><a>Meet John</a>
</div>
<div class="abs amb" style="top:945px;height:45px">
  <div class="avatar"><span style="background:#8a8a8a" role="img" aria-label="Ambassador portrait"></span></div>
  <h4>Jane Smith</h4><p>Lorem ipsum dolor sit amet, consectetur</p><a>Jane Smith</a>
</div>
<div class="abs amb" style="top:1010px;height:45px">
  <div class="avatar"><span style="background:#7fbb14" role="img" aria-label="Ambassador portrait"></span></div>
  <h4>John Doe</h4><p>Lorem ipsum dolor sit amet, consectetur</p><a>Meet John</a>
</div>

<footer class="abs footer"></footer>
<div class="abs foot-links">Home &nbsp;|&nbsp; About Us &nbsp;|&nbsp; Resources &nbsp;|&nbsp; Article &nbsp;|&nbsp; Work-shops &nbsp;|&nbsp; Ambassadors &nbsp;|&nbsp; Feats</div>
<div class="abs foot-copy">Brook Rise ©</div>
<div class="abs contact-icon" role="img" aria-label="Address book icon"></div>
<div class="abs contact-title"><b>Contact</b> info:</div>
<div class="abs contact-rule"></div>
<address class="abs address" style="font-style:normal">Calle Olmos 52, Col. Valle Verde<br>Saltillo, Coah. 25010</address>
</body>
</html>
```